Baby Shower Invitation for Vectored Image Provided

Caroline & Desmond's Baby Shower - Black/White/Gold Colors preferred
Please use the vectored portrait image attached. I'd like us on the lower right side of the invitation.
Can be horizontal or vertical layout.
The second image attached has the information needed for you to complete.
I don't want that style copied, it is just an example.

```html
<!DOCTYPE html>
<html lang="en">
<head>
<meta charset="utf-8">
<title>Oh Boy! Baby Shower Invitation</title>
<link rel="stylesheet" href="https://fonts.googleapis.com/css2?family=Kaushan+Script&family=Cutive&display=swap">
<style>
  :root {
    --gold: #c8a765;
    --ink: #111111;
    --paper: #ffffff;
    --stripe-black: #0c0c0c;
    --stripe-gold: #c9a86a;
    --portrait-dark: #1c1c1e;
    --portrait-skin: #c99a84;
  }
  * { margin: 0; padding: 0; box-sizing: border-box; }
  html, body { width: 846px; height: 1200px; overflow: hidden; }
  body {
    background: repeating-linear-gradient(
      -45deg,
      var(--stripe-gold) 0 28px,
      var(--paper) 28px 56px,
      var(--stripe-black) 56px 84px,
      var(--paper) 84px 112px
    );
    position: relative;
  }
  .invitation-card {
    position: absolute;
    left: 58px; top: 60px;
    width: 728px; height: 1080px;
    background: var(--paper);
    box-shadow: 0 2px 6px rgba(0,0,0,0.35);
    font-family: "Cutive", "Courier New", serif;
    color: var(--ink);
  }
  .headline {
    position: absolute; left: 0; right: 0; top: 40px;
    text-align: center;
    font-family: "Kaushan Script", cursive;
    font-size: 96px; line-height: 1;
    color: var(--gold);
  }
  .ribbon { position: absolute; left: 131px; top: 166px; width: 470px; height: 66px; }
  .ribbon-text {
    font-family: "Cutive", "Courier New", serif;
    font-size: 22px; fill: var(--paper);
  }
  .intro {
    position: absolute; left: 0; right: 0; top: 266px;
    text-align: center; font-size: 25px; line-height: 39px;
  }
  .honoree {
    position: absolute; left: 30px; right: 0; top: 372px;
    text-align: center;
    font-family: "Kaushan Script", cursive;
    font-size: 74px; line-height: 1;
    color: var(--gold);
  }
  .rule-dotted {
    position: absolute; left: 53px; width: 624px; height: 0;
    border-top: 3px dotted var(--ink);
  }
  .rule-top { top: 498px; }
  .rule-bottom { top: 700px; }
  .rule-mid { top: 637px; left: 252px; width: 425px; }
  .rule-vertical {
    position: absolute; left: 227px; top: 514px; height: 172px; width: 0;
    border-left: 3px dotted var(--ink);
  }
  .date-block {
    position: absolute; left: 40px; top: 510px; width: 180px; text-align: center;
  }
  .date-day { font-family: "Kaushan Script", cursive; font-size: 34px; line-height: 44px; }
  .date-month { font-size: 46px; line-height: 52px; color: var(--gold); letter-spacing: 2px; font-weight: bold; }
  .date-number { font-size: 76px; line-height: 74px; color: var(--gold); }
  .venue-name {
    position: absolute; left: 252px; width: 425px; top: 520px; text-align: center;
    font-family: "Kaushan Script", cursive; font-size: 50px; line-height: 1;
  }
  .venue-address {
    position: absolute; left: 252px; width: 425px; top: 588px; text-align: center;
    font-size: 25px; color: var(--gold);
  }
  .event-time {
    position: absolute; left: 252px; width: 425px; top: 650px; text-align: center;
    font-size: 30px; color: var(--gold);
  }
  .rsvp {
    position: absolute; left: 53px; top: 772px;
    font-size: 24px; line-height: 34px;
  }
  .rsvp sup { font-size: 13px; }
  .registry {
    position: absolute; left: 53px; top: 922px;
    font-family: "Kaushan Script", cursive;
    font-size: 30px; line-height: 44px; color: var(--gold);
  }
  .couple-portrait {
    position: absolute; left: 418px; top: 724px; width: 272px; height: 356px;
    border-radius: 120px 120px 0 0;
    background: linear-gradient(180deg, var(--portrait-skin) 0%, #7a5e52 35%, var(--portrait-dark) 70%);
  }
</style>
</head>
<body>
  <main class="invitation-card">
    <h1 class="headline">Oh Boy!</h1>

    <svg class="ribbon" viewBox="0 0 470 66" aria-hidden="false">
      <path d="M0 22 Q235 -6 470 10 L446 34 L466 60 Q235 44 6 66 L28 44 Z" fill="var(--gold)"/>
      <text class="ribbon-text" x="235" y="44" text-anchor="middle">A Little Man Is On The Way!</text>
    </svg>

    <p class="intro">Please join us for a<br>Baby Shower honoring</p>

    <h2 class="honoree">Caroline Westerhall</h2>

    <div class="rule-dotted rule-top"></div>
    <div class="rule-vertical"></div>

    <div class="date-block">
      <div class="date-day">Saturday</div>
      <div class="date-month">SEPT</div>
      <div class="date-number">1</div>
    </div>

    <div class="venue-name">The Willowmere</div>
    <div class="venue-address">1846 Linden Ave. Raleigh, NC</div>
    <div class="rule-dotted rule-mid"></div>
    <div class="event-time">11:30am - 2:30pm</div>

    <div class="rule-dotted rule-bottom"></div>

    <p class="rsvp">RSVP to Desmond<br>at 919 555 0148<br>by 20<sup>th</sup> August</p>

    <p class="registry">Caroline is registered<br>at Little Nest Baby</p>

    <div class="couple-portrait" role="img" aria-label="Illustrated portrait of the expecting couple standing together, his hands on her baby bump"></div>
  </main>
</body>
</html>
```